Startup online payment business - Sporting / Golf, Swift Tee payment

Background:
Our business name is "Swift Tee" we provide online payments for golfing services via our website. We currently have a logo used on our website. No other design style has been developed. Our aim is to remove cash payments for service at golf clubs.

Our Key Values:
Quick and easy
Formal and polite
Fun with professional boundary
Mate-ship relationships
100% online digital

What we want from you:
Marketing design to be used on posters and stickers in a retail setting to direct customers to our online payment Chanel.
Design must incorporate attached logo, URL swifttee.com.au and our key values can act as a guide the type of design. We have used color Hex#007672 for logo background. We are open to use other colors.

Target Market(s)

Golf clubs and golf players

Industry/Entity Type

Golf Course

Font styles to use
Sans Serif

Requirements
Must have
• Directions to online payment via URL: swifttee.com.au
Nice to have
• We like the idea of the slogan: No Cash - No worries. Have attached home screen that will be available from URL link. Consideration if using mobile phone in image. Push the online payment and steps 1. Visit swifttee.com 2. Select club 3. Confirm payment
Should not have
• Cartoons

```html
<!DOCTYPE html>
<html lang="en">
<head>
<meta charset="utf-8">
<title>Swift Tee – No Cash? No Worries!</title>
<link rel="stylesheet" href="https://fonts.googleapis.com/css2?family=Bebas+Neue&family=Fira+Sans:ital,wght@0,400;0,500;0,700;1,400&display=swap">
<style>
  :root {
    --teal: #007672;
    --teal-dark: #04605c;
    --cream: #fffdc9;
    --grass-light: #a9c65a;
    --grass: #5f8f24;
    --grass-dark: #2f5a12;
    --lime: #d7dc3c;
    --ink: #141414;
    --grey-text: #6f6f6f;
    --stage: #8b8b8b;
    --white: #ffffff;
  }
  * { box-sizing: border-box; margin: 0; padding: 0; }
  html, body { width: 958px; height: 1200px; overflow: hidden; background: var(--stage); }
  body { position: relative; font-family: "Fira Sans", Arial, sans-serif; }

  .poster {
    position: absolute; left: 115px; top: 61px;
    width: 729px; height: 1031px;
    background: var(--cream);
    overflow: hidden;
  }

  .golf-scene {
    position: absolute; left: 0; top: 440px; width: 729px; height: 492px;
    background: linear-gradient(180deg, rgba(255,253,201,0) 0%, var(--grass-light) 14%, var(--grass) 48%, var(--grass-dark) 100%);
  }
  .phone-in-hand {
    position: absolute; left: 420px; top: 378px; width: 309px; height: 455px;
    border-radius: 28px 28px 0 60px;
    background: linear-gradient(160deg, #eeeeee 0%, #d9d9d9 18%, #1b7f79 32%, #117670 70%, #e6b58f 100%);
    opacity: .9;
  }

  .headline {
    position: absolute; left: 124px; top: 64px;
    font-family: "Bebas Neue", "Arial Narrow", sans-serif;
    line-height: .84;
    background: linear-gradient(200deg, #6e8a1f 0%, #28400d 30%, #0a0d05 55%, #0a0d05 75%, #3f7a14 100%);
    -webkit-background-clip: text; background-clip: text;
    color: transparent;
  }
  .headline__line--top { display: block; font-size: 167px; letter-spacing: -1px; }
  .headline__line--bottom { display: block; font-size: 124px; letter-spacing: -1px; margin-top: 8px; }

  .values-tag {
    position: absolute; left: 125px; top: 379px; width: 193px; height: 27px;
    background: var(--teal);
    clip-path: polygon(0 0, 94% 0, 100% 100%, 0 100%);
    color: var(--lime); font-weight: 700; font-size: 20px; line-height: 27px;
    padding-left: 7px; letter-spacing: .2px;
  }
  .values-list { position: absolute; left: 123px; top: 433px; list-style: none; }
  .values-list__item {
    position: relative; padding-left: 31px;
    font-size: 19.5px; font-weight: 500; color: var(--ink); line-height: 22px;
    margin-bottom: 13px;
  }
  .values-list__item--wrap { margin-bottom: 14px; }
  .values-list__item svg { position: absolute; left: 0; top: 1px; }

  .footer-band { position: absolute; left: 0; top: 0; }

  .step { position: absolute; width: 150px; text-align: center; }
  .step__icon {
    width: 82px; height: 82px; margin: 0 auto; border-radius: 50%;
    background: var(--white); display: flex; align-items: center; justify-content: center;
  }
  .step__label { margin-top: 11px; color: var(--teal); font-size: 15.5px; font-weight: 500; white-space: nowrap; }
  .step--visit { left: 34px; top: 816px; }
  .step--club { left: 169px; top: 816px; }
  .step--pay { left: 295px; top: 816px; }

  .site-url {
    position: absolute; left: 34px; top: 979px; width: 175px; height: 21px;
    background: var(--teal); color: var(--white);
    font-size: 20px; font-weight: 700; line-height: 21px; text-align: center;
  }
  .tagline {
    position: absolute; left: 265px; top: 977px; width: 210px; text-align: center;
    font-size: 17px; font-style: italic; color: var(--grey-text);
  }
  .brand-box {
    position: absolute; left: 540px; top: 914px; width: 168px; height: 117px;
    background: var(--teal);
    display: flex; align-items: center; justify-content: center;
    color: var(--white); font-size: 27px; font-weight: 700;
  }
</style>
</head>
<body>
  <main class="poster">
    <div class="golf-scene" role="img" aria-label="Photo of a golf iron and ball resting on a grassy fairway"></div>
    <div class="phone-in-hand" role="img" aria-label="Photo of a hand holding a smartphone showing the Swift Tee payment screen"></div>

    <h1 class="headline">
      <span class="headline__line--top">NO CASH?</span>
      <span class="headline__line--bottom">NO WORRIES!</span>
    </h1>

    <div class="values-tag">OUR KEY VALUES</div>
    <ul class="values-list">
      <li class="values-list__item"><svg width="21" height="21" viewBox="0 0 20 20"><circle cx="10" cy="10" r="10" fill="#007672"/><path d="M5.5 10.3l3 3 6-6.5" fill="none" stroke="#d7dc3c" stroke-width="2.2" stroke-linecap="round" stroke-linejoin="round"/></svg>Quick and easy</li>
      <li class="values-list__item"><svg width="21" height="21" viewBox="0 0 20 20"><circle cx="10" cy="10" r="10" fill="#007672"/><path d="M5.5 10.3l3 3 6-6.5" fill="none" stroke="#d7dc3c" stroke-width="2.2" stroke-linecap="round" stroke-linejoin="round"/></svg>Formal and polite</li>
      <li class="values-list__item values-list__item--wrap"><svg width="21" height="21" viewBox="0 0 20 20"><circle cx="10" cy="10" r="10" fill="#007672"/><path d="M5.5 10.3l3 3 6-6.5" fill="none" stroke="#d7dc3c" stroke-width="2.2" stroke-linecap="round" stroke-linejoin="round"/></svg>Fun with professional<br>boundary</li>
      <li class="values-list__item"><svg width="21" height="21" viewBox="0 0 20 20"><circle cx="10" cy="10" r="10" fill="#007672"/><path d="M5.5 10.3l3 3 6-6.5" fill="none" stroke="#d7dc3c" stroke-width="2.2" stroke-linecap="round" stroke-linejoin="round"/></svg>Mate-ship relationships</li>
      <li class="values-list__item"><svg width="21" height="21" viewBox="0 0 20 20"><circle cx="10" cy="10" r="10" fill="#007672"/><path d="M5.5 10.3l3 3 6-6.5" fill="none" stroke="#d7dc3c" stroke-width="2.2" stroke-linecap="round" stroke-linejoin="round"/></svg>100% online digital</li>
    </ul>

    <svg class="footer-band" width="729" height="1031" viewBox="0 0 729 1031">
      <polygon points="0,930 481,930 534,893 729,893 729,1031 0,1031" fill="#ffffff"/>
      <line x1="496" y1="869" x2="532" y2="833" stroke="#007672" stroke-width="7"/>
    </svg>

    <div class="step step--visit">
      <div class="step__icon">
        <svg width="62" height="62" viewBox="0 0 62 62" fill="none" stroke="#007672" stroke-width="4">
          <circle cx="31" cy="31" r="27"/>
          <ellipse cx="31" cy="31" rx="12" ry="27"/>
          <line x1="31" y1="4" x2="31" y2="58"/>
          <rect x="2" y="23" width="58" height="16" fill="#fff" stroke="none"/>
          <text x="31" y="36" text-anchor="middle" font-family="Fira Sans, sans-serif" font-weight="700" font-size="13" fill="#007672" stroke="none">WWW</text>
        </svg>
      </div>
      <div class="step__label">Visit swifttee.com</div>
    </div>

    <div class="step step--club">
      <div class="step__icon">
        <svg width="60" height="62" viewBox="0 0 60 62" fill="#007672">
          <circle cx="30" cy="9" r="6" fill="none" stroke="#007672" stroke-width="3"/>
          <circle cx="11" cy="20" r="6" fill="none" stroke="#007672" stroke-width="3"/>
          <circle cx="49" cy="20" r="6" fill="none" stroke="#007672" stroke-width="3"/>
          <rect x="26" y="22" width="7" height="22" rx="3.5"/>
          <rect x="24" y="38" width="22" height="22" rx="5"/>
        </svg>
      </div>
      <div class="step__label">Select club</div>
    </div>

    <div class="step step--pay">
      <div class="step__icon">
        <svg width="60" height="60" viewBox="0 0 60 60" fill="none" stroke="#007672" stroke-width="4">
          <rect x="14" y="5" width="38" height="26" rx="3"/>
          <line x1="14" y1="13" x2="52" y2="13"/>
          <circle cx="32" cy="30" r="8" fill="#007672" stroke="#fff" stroke-width="2"/>
          <rect x="6" y="38" width="8" height="18" fill="#007672" stroke="none"/>
          <path d="M14 42h14l10 6 14-6" stroke-linecap="round" stroke-linejoin="round"/>
        </svg>
      </div>
      <div class="step__label">Confirm payment</div>
    </div>

    <div class="site-url">swifttee.com.au</div>
    <p class="tagline">Safer and faster way to pay</p>
    <div class="brand-box">Swift Tee</div>
  </main>
</body>
</html>
```